Flyer-Design für Immobilienmakler
Zielgruppe
Wir sind Immobilienmakler und die Zielgruppe sind Immobilieneigentümer. Mit dem Flyer wollen wir kreative und evtl. auch 'freche' art auf uns aufmernksammachen, dass der Verkaufwillige sich an uns wendet.
Aufgabenstellung
Was wir nicht wollen: Flyer wie sie alle machen...ala wir sind die Tollsten und Besten.
Die Flyerform kann gerne besonders sein.
Unser Farben:
Blau R33 G49 B98
Rot R201 G0 B25
Unsere 'Wanda' und das Logo sende ich Ihnen als JPG.
Die Vektordatei reiche ich nach

```html
<!DOCTYPE html>
<html lang="de">
<head>
<meta charset="utf-8">
<title>Heimhafen Immobilien – Flyer</title>
<link href="https://fonts.googleapis.com/css2?family=Catamaran:wght@600;700&family=Questrial&display=swap" rel="stylesheet">
<style>
:root{
  --brand-blue:#372f61;
  --brand-red:#c90019;
  --paper:#ffffff;
  --ink:#2c2a3a;
  --page-bg:#ffffff;
}
*{margin:0;padding:0;box-sizing:border-box}
html,body{width:1200px;height:1200px;overflow:hidden;background:var(--page-bg)}
body{position:relative;font-family:"Questrial",sans-serif;color:var(--ink)}
.panel{position:absolute;background:var(--paper);box-shadow:3px 4px 6px rgba(0,0,0,.35);overflow:hidden}
.panel--outer-wide{left:25px;top:61px;width:760px;height:381px}
.panel--outer-narrow{left:807px;top:61px;width:376px;height:381px}
.panel--inner-wide{left:25px;top:532px;width:760px;height:379px}
.panel--inner-narrow{left:807px;top:532px;width:376px;height:379px}

.band{position:absolute;left:0;right:0;top:191px;bottom:0;background:var(--brand-blue)}
.panel--inner-narrow .band{top:190px}

.company-title{position:absolute;font-family:"Catamaran",sans-serif;font-weight:700;color:var(--brand-blue);font-size:19px;text-align:center;white-space:nowrap}
.title-rule{position:absolute;height:2px;width:100px;background:var(--brand-blue)}
.slogan{position:absolute;font-family:"Catamaran",sans-serif;font-weight:700;color:var(--brand-blue);font-size:18.5px;white-space:nowrap;text-align:center}
.slogan .accent{color:var(--brand-red)}

.brand{position:absolute;top:26px;right:22px;display:flex;align-items:center;gap:4px;font-family:"Questrial",sans-serif;color:var(--brand-blue);font-size:14px;white-space:nowrap}
.brand-dot{width:7px;height:7px;border-radius:50%;background:var(--brand-red)}

.photo{position:absolute}
.photo--peeking{top:82px;height:109px;background:linear-gradient(180deg,#f4f1ef 0%,#d8c6bb 55%,#9a8476 100%);border-radius:40px 40px 0 0}
.photo--building{left:0;top:0;width:760px;height:126px;background:linear-gradient(100deg,#6a5560 0%,#b8a9b4 35%,#8aa5c8 60%,#1e5aa8 85%,#2a77c9 100%)}

.offices{position:absolute;top:267px;display:flex;color:#fff;font-size:8.2px;line-height:9.8px}
.office{width:164px;white-space:nowrap}
.office-head{font-family:"Catamaran",sans-serif;font-weight:700;font-size:8.2px;letter-spacing:.2px;text-transform:uppercase;margin-bottom:12px}
.office-name{margin-bottom:10px}

.callout{position:absolute;top:246px;font-family:"Catamaran",sans-serif;font-weight:700;color:#fff;font-size:17.5px;line-height:24px;white-space:nowrap}
.callout span{display:inline-block;background:var(--brand-red);padding:0 11px}
.callout .l1{padding-right:13px}
.callout .l2{margin-top:-1px}
.callout .l3{display:block;width:fit-content;margin:5px 0 0 auto;padding:0 11px;line-height:25px;text-transform:uppercase}

.col{position:absolute;top:146px;width:168px;font-size:7.9px;line-height:9.7px;color:#333;hyphens:auto}
.col--1{left:20px}
.col--2{left:195px}
.col--3{left:400px}
.col--4{left:575px}
.col h3{font-family:"Catamaran",sans-serif;font-weight:700;font-size:8.4px;line-height:10px;color:var(--brand-blue);text-transform:uppercase;margin-bottom:4px}
.col p{margin-bottom:13px}
</style>
</head>
<body>

<!-- Outside spread -->
<section class="panel panel--outer-wide">
  <h1 class="company-title" style="left:0;width:380px;top:65px">Heimhafen Immobilien GmbH</h1>
  <div class="title-rule" style="left:140px;top:100px"></div>
  <p class="slogan" style="left:0;width:380px;top:114px">Besser w<span class="accent">o</span>hnen – Besser leben!</p>
  <div class="brand">Heimhafen Immobilien<span class="brand-dot"></span></div>
  <div class="photo photo--peeking" style="left:405px;width:330px" role="img" aria-label="Foto: Mann mit Brille schaut mit großen Augen über die Kante, die Hände am Rand"></div>
  <div class="band"></div>
  <div class="offices" style="left:45px">
    <div class="office">
      <div class="office-head">Hauptgeschäftsstelle Nordstadt</div>
      <div class="office-name">Heimhafen Immobilien GmbH</div>
      <div>Lindenweg 12<br>21000 Nordstadt<br>info@heimhafen-beispiel.de<br>Tel. &nbsp;+49 4100-1234500<br>Fax. +49 4100-1234501</div>
    </div>
    <div class="office">
      <div class="office-head">Filiale Südheim</div>
      <div class="office-name">Heimhafen Immobilien GmbH</div>
      <div>Marktplatz 4<br>21600 Südheim<br>suedheim@heimhafen-beispiel.de<br>Tel. &nbsp;+49 4160-5678900<br>Fax. +49 4160-5678901</div>
    </div>
  </div>
  <div class="callout" style="left:427px">
    <span class="l1">Damit Ihnen der Haus verkauf</span><br>
    <span class="l2">nicht über den Kopf wächst.</span>
    <span class="l3">Wir beraten Sie gerne!</span>
  </div>
</section>

<section class="panel panel--outer-narrow">
  <div class="brand">Heimhafen Immobilien<span class="brand-dot"></span></div>
  <div class="photo photo--peeking" style="left:18px;width:340px" role="img" aria-label="Foto: Mann mit Brille schaut mit großen Augen über die Kante, die Hände am Rand"></div>
  <div class="band"></div>
  <div class="callout" style="left:42px">
    <span class="l1">Damit Ihnen der Haus verkauf</span><br>
    <span class="l2">nicht über den Kopf wächst.</span>
    <span class="l3">Wir beraten Sie gerne!</span>
  </div>
</section>

<!-- Inside spread -->
<section class="panel panel--inner-wide">
  <div class="photo photo--building" role="img" aria-label="Foto: moderne Bürofassade mit geschwungenen Fensterbändern, von unten fotografiert"></div>
  <div class="col col--1">
    <h3>Lorem ipsum</h3>
    <p>Lorem ipsum dolor sit amet, consectetuer adipiscing elit. Aenean commodo ligula eget dolor. Aenean massa. Cum sociis natoque penatibus et magnis dis parturient montes, nascetur ridiculus mus. Donec quam felis, ultricies nec, pellentesque eu, pretium quis, sem. Nulla consequat massa quis enim. Donec pede justo, fringilla vel, aliquet nec, vulputate eget, arcu. In enim justo, rhoncus ut, imperdiet a, venenatis vitae, justo. Nullam dictum felis eu pede mollis pretium. Integer tincidunt. Cras dapibus.</p>
    <h3>Lorem ipsum</h3>
    <p>Vivamus elementum semper nisi. Aenean vulputate eleifend tellus. Aenean leo ligula, porttitor eu, consequat vitae, eleifend ac, enim. Aliquam lorem ante, dapibus</p>
  </div>
  <div class="col col--2">
    <p>in, viverra quis, feugiat a, tellus. Phasellus viverra nulla ut metus varius laoreet. Quisque rutrum. Aenean imperdiet. Etiam ultricies nisi vel augue. Curabitur ullamcorper ultricies nisi. Nam eget dui. Etiam rhoncus. Maecenas tempus, tellus eget condimentum rhoncus, sem quam semper libero, sit amet adipiscing sem neque sed ipsum.</p>
    <h3>Lorem ipsum</h3>
    <p>Nam quam nunc, blandit vel, luctus pulvinar, hendrerit id, lorem. Maecenas nec odio et ante tincidunt tempus. Donec vitae sapien ut libero venenatis faucibus. Nullam quis ante. Etiam sit amet orci eget eros faucibus tincidunt. Duis leo</p>
  </div>
  <div class="col col--3">
    <h3>Lorem ipsum</h3>
    <p>Lorem ipsum dolor sit amet, consectetuer adipiscing elit. Aenean commodo ligula eget dolor. Aenean massa. Cum sociis natoque penatibus et magnis dis parturient montes, nascetur ridiculus mus. Donec quam felis, ultricies nec, pellentesque eu, pretium quis, sem. Nulla consequat massa quis enim. Donec pede justo, fringilla vel, aliquet nec, vulputate eget, arcu. In enim justo, rhoncus ut, imperdiet a, venenatis vitae, justo. Nullam dictum felis eu pede mollis pretium. Integer tincidunt. Cras dapibus.</p>
    <h3>Lorem ipsum</h3>
    <p>Vivamus elementum semper nisi. Aenean vulputate eleifend tellus. Aenean leo ligula, porttitor eu, consequat vitae, eleifend ac, enim. Aliquam lorem ante, dapibus</p>
  </div>
  <div class="col col--4">
    <p>in, viverra quis, feugiat a, tellus. Phasellus viverra nulla ut metus varius laoreet. Quisque rutrum. Aenean imperdiet. Etiam ultricies nisi vel augue. Curabitur ullamcorper ultricies nisi. Nam eget dui. Etiam rhoncus. Maecenas tempus, tellus eget condimentum rhoncus, sem quam semper libero, sit amet adipiscing sem neque sed ipsum.</p>
    <h3>Lorem ipsum</h3>
    <p>Nam quam nunc, blandit vel, luctus pulvinar, hendrerit id, lorem. Maecenas nec odio et ante tincidunt tempus. Donec vitae sapien ut libero venenatis faucibus. Nullam quis ante. Etiam sit amet orci eget eros faucibus tincidunt. Duis leo</p>
  </div>
</section>

<section class="panel panel--inner-narrow">
  <h2 class="company-title" style="left:0;width:376px;top:64px">Heimhafen Immobilien GmbH</h2>
  <div class="title-rule" style="left:138px;top:99px"></div>
  <p class="slogan" style="left:0;width:376px;top:113px">Besser w<span class="accent">o</span>hnen – Besser leben!</p>
  <div class="band"></div>
  <div class="offices" style="left:44px;top:266px">
    <div class="office">
      <div class="office-head">Hauptgeschäftsstelle Nordstadt</div>
      <div class="office-name">Heimhafen Immobilien GmbH</div>
      <div>Lindenweg 12<br>21000 Nordstadt<br>info@heimhafen-beispiel.de<br>Tel. &nbsp;+49 4100-1234500<br>Fax. +49 4100-1234501</div>
    </div>
    <div class="office">
      <div class="office-head">Filiale Südheim</div>
      <div class="office-name">Heimhafen Immobilien GmbH</div>
      <div>Marktplatz 4<br>21600 Südheim<br>suedheim@heimhafen-beispiel.de<br>Tel. &nbsp;+49 4160-5678900<br>Fax. +49 4160-5678901</div>
    </div>
  </div>
</section>

</body>
</html>
```